Slider needed for Database Documentation Topic

We need a slider to promote a content area of a web site. I'm listing this as a poster because the posters I have seen on Quillbarn portfolios most closely resemble the combination or art and text I am looking for.
The content area we are promoting with this graphic will clarify the design and use of a complicated database. The title of the content area is "The Marbled QZ Database" and the banner should use that title.
To 'illuminate' something means to cast light on it, and this content area will help shed light on a complicated thing – the content will use diagrams, text, and examples to clarify the database. Another meaning is that an illuminated manuscript is a manuscript brought to life with pictures, and in a way that is also what this content area will do.
One idea for the slider might be a light bulb, lamp, candle or flashlight lighting up the words "QZ Database". Another idea would be the type of illustration you see if you search for "Illuminated manuscript"
But I'm not committed to any particular idea - in the past I have been pleased to see ideas that are different than my own but accomplish the same thing, so please feel free to use your judgement or ask any questions.
In addition to the title (The Marbled QZ Database) the graphic should allow room for three smaller lines of text – the three bullet items below:
- Guide to understanding the QZ database
- Data sources, uses and relationships explained with illustrations
- New content! Customers
The last bullet item will change as the content is added.
Some particulars ...
SIZE - 600 high x 1200 wide pixels
PHOTOS vs ILLUSTRATION - I am open to either one.

```html
<!DOCTYPE html>
<html lang="en">
<head>
<meta charset="utf-8">
<title>The Marbled QZ Database</title>
<link rel="stylesheet" href="https://fonts.googleapis.com/css2?family=UnifrakturCook:wght@700&display=swap">
<style>
  :root {
    --night: #000000;
    --ember: #1c1203;
    --glow: #6b4a10;
    --warm: #a47a2c;
    --gold-text: #f6dc96;
    --gold-mark: #e8c774;
    --gold-edge: #3b2503;
  }
  * { margin: 0; padding: 0; box-sizing: border-box; }
  html, body {
    width: 1200px;
    height: 600px;
    overflow: hidden;
    background: var(--night);
  }
  .slider {
    position: relative;
    width: 1200px;
    height: 600px;
    overflow: hidden;
    background: var(--night);
  }
  .backdrop-photo {
    position: absolute;
    inset: 0;
    background: radial-gradient(ellipse 560px 520px at 220px 260px, var(--warm) 0, var(--glow) 35%, var(--ember) 70%, var(--night) 100%);
  }
  .content {
    position: absolute;
    left: 440px;
    top: 0;
    width: 700px;
    height: 600px;
    font-family: "UnifrakturCook", "Times New Roman", serif;
    color: var(--gold-text);
  }
  .title {
    position: absolute;
    left: 0;
    top: 84px;
    width: 680px;
    text-align: center;
    font-size: 50px;
    font-weight: 700;
    letter-spacing: 3px;
    text-shadow:
      2px 2px 0 var(--gold-edge), -2px -2px 0 var(--gold-edge),
      2px -2px 0 var(--gold-edge), -2px 2px 0 var(--gold-edge),
      0 0 12px rgba(255, 190, 80, 0.35);
  }
  .points { list-style: none; }
  .point {
    position: absolute;
    left: 45px;
    display: flex;
    align-items: flex-start;
    font-size: 27px;
    font-weight: 700;
    letter-spacing: 2.5px;
    line-height: 40px;
    white-space: nowrap;
    text-shadow: 1px 1px 0 var(--gold-edge), 0 0 6px rgba(0, 0, 0, 0.8);
  }
  .point--guide { top: 206px; }
  .point--sources { top: 298px; }
  .point--latest { top: 418px; }
  .point-mark {
    flex: none;
    width: 18px;
    height: 30px;
    margin: 4px 30px 0 0;
    background: var(--gold-mark);
  }
  .point-text { text-align: center; }
</style>
</head>
<body>
  <main class="slider">
    <div class="backdrop-photo" role="img" aria-label="Photograph of a lit pillar candle glowing in the dark with soft lens flares"></div>
    <section class="content">
      <h1 class="title">The Marbled QZ Database</h1>
      <ul class="points">
        <li class="point point--guide">
          <span class="point-mark" role="img" aria-label="Quill leaf ornament"></span>
          <span class="point-text">Guide to understanding the QZ database.</span>
        </li>
        <li class="point point--sources">
          <span class="point-mark" role="img" aria-label="Quill leaf ornament"></span>
          <span class="point-text">Data sources, uses and relationships<br>explained with illustrations.</span>
        </li>
        <li class="point point--latest">
          <span class="point-mark" role="img" aria-label="Quill leaf ornament"></span>
          <span class="point-text">New content! Customers.</span>
        </li>
      </ul>
    </section>
  </main>
</body>
</html>
```